Finance Flyer/ brouchure Design

I would a finance flyer/ brouchure deisgned detailing the services that we offer as per the below.
Lending & Leasing
General Insurance
Risk Insurance
Wealth Planning
Commercial, Equipment & Asset Finance
I would also like the brouchure to state that 'we have access to over 35 lenders', 'Our services are free to you', 'We will find you the best deal & make it easy for you'.
I would like a spot on the flyer/ brouchure where I can place a picture of the local finance broker and a short bio on them.
I would like to be able to come back to the person ultimately chosen to design a suite of flyers.

Target Market(s)

My target auidience are families, aged between 30 & 50 with children.
I would like the flyer to appear professional but friendly and to work with the colours of my logo.

Industry/Entity Type

Finance

Font styles to use
Serif

Colors

Designer to choose colors to be used in the design.

Requirements
Must have
• Be friendly & inviting
• Work with the colours of my logo
• Call to action - 'Call us today on 1300 482 615'
• Must have a Contact us section including the following
• Phone number- 1300 482 615
• Location- Brisbane & surrounds
• Email- Moira@tallowbq.com.au
• Website- www.tallowbq.com.au
• Facebook- www.facebook.com/tallowmonetary

```html
<!DOCTYPE html>
<html lang="en">
<head>
<meta charset="utf-8">
<title>Tallow BQ Finance Flyer</title>
<link rel="stylesheet" href="https://fonts.googleapis.com/css2?family=Fira+Sans+Condensed:wght@600;700&family=Fira+Sans:wght@600&family=Source+Sans+3:ital,wght@0,400;0,600;1,400&display=swap">
<style>
  :root {
    --teal: #154f5d;
    --green: #8dc63f;
    --text: #555a5c;
    --white: #ffffff;
  }
  * { box-sizing: border-box; margin: 0; padding: 0; }
  html, body { width: 978px; height: 1200px; overflow: hidden; background: var(--white); }
  .flyer {
    position: relative; width: 978px; height: 1200px; overflow: hidden;
    background: var(--white); font-family: "Source Sans 3", sans-serif; color: var(--text);
  }
  .hero-art { position: absolute; left: 0; top: 0; }
  .brand {
    position: absolute; left: 73px; top: 120px; width: 290px;
    display: flex; align-items: center; gap: 12px;
    font-family: "Fira Sans Condensed", sans-serif; font-weight: 700;
    font-size: 40px; letter-spacing: 2px; color: var(--teal);
  }
  .brand-mark { width: 26px; height: 26px; background: var(--green); flex: none; }
  .headline {
    position: absolute; left: 16px; top: 222px; width: 400px; text-align: center;
    font-family: "Fira Sans Condensed", sans-serif; font-weight: 700;
    font-size: 38px; line-height: 43px; color: var(--teal); text-transform: uppercase;
  }
  .headline .accent { color: var(--green); }
  .services { position: absolute; left: 34px; top: 362px; list-style: none; }
  .services li {
    display: flex; align-items: center; gap: 16px;
    font-size: 27px; line-height: 37.5px; color: var(--text);
  }
  .services svg { width: 22px; height: 22px; flex: none; }
  .free-badge {
    position: absolute; left: 547px; top: 364px; width: 216px; height: 216px;
    border-radius: 50%; background: var(--teal); border: 7px solid var(--white);
    display: flex; align-items: center; justify-content: center; text-align: center;
    font-family: "Fira Sans", sans-serif; font-weight: 600; font-size: 25px; line-height: 36px;
    color: var(--white); text-transform: uppercase;
  }
  .lenders {
    position: absolute; left: 0; top: 598px; width: 978px; text-align: center;
    font-family: "Fira Sans Condensed", sans-serif; font-weight: 700; font-size: 39px;
    color: var(--teal); text-transform: uppercase;
  }
  .lenders-note {
    position: absolute; left: 0; top: 646px; width: 978px; text-align: center;
    font-size: 20px; line-height: 21px; color: var(--text);
  }
  .photo-strip { position: absolute; left: 34px; top: 715px; }
  .broker-card {
    position: absolute; left: 34px; top: 911px; width: 912px; height: 186px;
    background: var(--teal); border-radius: 0 0 32px 32px; color: var(--white);
  }
  .broker-photo {
    position: absolute; left: 30px; top: 14px; width: 156px; height: 156px; border-radius: 50%;
    border: 5px solid var(--white);
    background: radial-gradient(circle at 50% 40%, #e8b896 0%, #c7704a 55%, #e9e4de 100%);
  }
  .broker-name { position: absolute; left: 218px; top: 12px; font-size: 23px; font-weight: 600; }
  .broker-role { position: absolute; left: 218px; top: 41px; font-size: 23px; }
  .social-dot {
    position: absolute; left: 832px; top: 13px; width: 58px; height: 58px;
    border-radius: 50%; background: var(--green);
  }
  .stars { position: absolute; left: 218px; top: 82px; font-size: 17px; color: #f7c21b; letter-spacing: 1px; }
  .review {
    position: absolute; left: 218px; top: 102px; width: 640px;
    font-style: italic; font-size: 18px; line-height: 23px;
  }
  .cta {
    position: absolute; left: 249px; top: 1086px; width: 477px; height: 48px;
    border-radius: 12px; background: var(--green); color: var(--white);
    display: flex; align-items: center; justify-content: center;
    font-family: "Fira Sans", sans-serif; font-weight: 600; font-size: 25px;
    box-shadow: 0 4px 8px rgba(0,0,0,0.2);
  }
  .contact {
    position: absolute; top: 1148px; display: flex; align-items: center; gap: 10px;
    font-size: 21px; font-weight: 600; color: var(--teal);
  }
  .contact svg { width: 20px; height: 20px; }
  .contact-email { left: 34px; }
  .contact-phone { left: 402px; }
  .contact-web { left: 684px; }
</style>
</head>
<body>
<main class="flyer">
  <svg class="hero-art" width="978" height="600" viewBox="0 0 978 600">
    <defs>
      <linearGradient id="heroTone" x1="0" y1="0" x2="0.4" y2="1">
        <stop offset="0" stop-color="#5a8fd6"/>
        <stop offset="0.45" stop-color="#cfd3d6"/>
        <stop offset="0.75" stop-color="#a9c9e0"/>
        <stop offset="1" stop-color="#5f9a3a"/>
      </linearGradient>
    </defs>
    <path d="M386,0 C380,200 450,420 640,520 C760,575 880,580 978,577 L978,0 Z" fill="var(--green)"/>
    <path d="M404,0 C398,190 460,380 630,470 C740,520 860,533 978,533 L978,0 Z" fill="url(#heroTone)" role="img" aria-label="Photo of a smiling family of three sitting on the lawn in front of their house"/>
  </svg>

  <div class="brand"><span class="brand-mark"></span>TALLOW BQ</div>

  <h1 class="headline">We will find you the<br>best deal &amp; make it<br><span class="accent">easy for you!</span></h1>

  <ul class="services">
    <li><svg viewBox="0 0 22 22"><circle cx="11" cy="11" r="9" fill="none" stroke="var(--teal)" stroke-width="2"/><path d="M6.5 11l3 3 6-6" fill="none" stroke="var(--teal)" stroke-width="2"/></svg>Lending &amp; Leasing</li>
    <li><svg viewBox="0 0 22 22"><circle cx="11" cy="11" r="9" fill="none" stroke="var(--teal)" stroke-width="2"/><path d="M6.5 11l3 3 6-6" fill="none" stroke="var(--teal)" stroke-width="2"/></svg>General Insurance</li>
    <li><svg viewBox="0 0 22 22"><circle cx="11" cy="11" r="9" fill="none" stroke="var(--teal)" stroke-width="2"/><path d="M6.5 11l3 3 6-6" fill="none" stroke="var(--teal)" stroke-width="2"/></svg>Risk Insurance</li>
    <li><svg viewBox="0 0 22 22"><circle cx="11" cy="11" r="9" fill="none" stroke="var(--teal)" stroke-width="2"/><path d="M6.5 11l3 3 6-6" fill="none" stroke="var(--teal)" stroke-width="2"/></svg>Wealth Planning</li>
    <li><svg viewBox="0 0 22 22"><circle cx="11" cy="11" r="9" fill="none" stroke="var(--teal)" stroke-width="2"/><path d="M6.5 11l3 3 6-6" fill="none" stroke="var(--teal)" stroke-width="2"/></svg>Commercial</li>
    <li><svg viewBox="0 0 22 22"><circle cx="11" cy="11" r="9" fill="none" stroke="var(--teal)" stroke-width="2"/><path d="M6.5 11l3 3 6-6" fill="none" stroke="var(--teal)" stroke-width="2"/></svg>Equipment &amp; Asset Finance</li>
  </ul>

  <div class="free-badge">Our<br>services are<br>free to you</div>

  <h2 class="lenders">We have access to over 35 lenders</h2>
  <p class="lenders-note">Your mortage brokeer works for you to get you the best rates, strategy, and advice<br>from dozens of different lenders!</p>

  <svg class="photo-strip" width="912" height="181" viewBox="0 0 912 181">
    <defs>
      <linearGradient id="beachTone" x1="0" y1="0" x2="1" y2="1">
        <stop offset="0" stop-color="#8fc4e6"/><stop offset="0.6" stop-color="#e3c3a6"/><stop offset="1" stop-color="#cfd9dd"/>
      </linearGradient>
      <linearGradient id="coupleTone" x1="0" y1="0" x2="1" y2="1">
        <stop offset="0" stop-color="#d9e6a0"/><stop offset="0.5" stop-color="#e6b493"/><stop offset="1" stop-color="#eceae6"/>
      </linearGradient>
      <linearGradient id="homeTone" x1="0" y1="0" x2="1" y2="1">
        <stop offset="0" stop-color="#f1ede6"/><stop offset="0.5" stop-color="#c9a88f"/><stop offset="1" stop-color="#6f6c73"/>
      </linearGradient>
    </defs>
    <polygon points="0,0 352,0 285,181 0,181" fill="url(#beachTone)" role="img" aria-label="Photo of a mother carrying her young child at the beach"/>
    <polygon points="361,0 575,0 508,181 294,181" fill="url(#coupleTone)" role="img" aria-label="Photo of a happy older couple embracing outdoors"/>
    <polygon points="584,0 912,0 912,181 517,181" fill="url(#homeTone)" role="img" aria-label="Photo of a young couple looking at a laptop on the couch"/>
  </svg>

  <section class="broker-card">
    <div class="broker-photo" role="img" aria-label="Portrait photo of the local finance broker"></div>
    <p class="broker-name">MOIRA DELACY</p>
    <p class="broker-role">Finance Specialist, Brisbane, Australia</p>
    <span class="social-dot"></span>
    <p class="stars">★★★★★</p>
    <p class="review">Moira made the home loan process so easy and uncomplicated. Would recommend her for any one looking to secure or refinance their home loan.<br>- Jenna Corliss</p>
  </section>

  <div class="cta">Call us today on 1300 482 615</div>

  <p class="contact contact-email"><svg viewBox="0 0 20 20"><circle cx="10" cy="10" r="8.5" fill="none" stroke="var(--teal)" stroke-width="1.6"/><rect x="5.5" y="7" width="9" height="6.5" fill="var(--teal)"/><path d="M5.5 7l4.5 3.5 4.5-3.5" fill="none" stroke="var(--white)" stroke-width="1"/></svg>Moira@tallowbq.com.au</p>
  <p class="contact contact-phone"><svg viewBox="0 0 20 20"><circle cx="10" cy="10" r="8.5" fill="none" stroke="var(--teal)" stroke-width="1.6"/><path d="M7 5.5l2 2-1 1.3c.6 1.3 1.7 2.4 3 3l1.3-1 2 2-1.3 1.5c-3.2-.4-6.3-3.5-6.7-6.7z" fill="var(--teal)"/></svg>1300 482 615</p>
  <p class="contact contact-web"><svg viewBox="0 0 20 20"><circle cx="10" cy="10" r="8.5" fill="none" stroke="var(--teal)" stroke-width="1.6"/><ellipse cx="10" cy="10" rx="3.5" ry="8.5" fill="none" stroke="var(--teal)" stroke-width="1.2"/><path d="M1.5 10h17M3 6h14M3 14h14" stroke="var(--teal)" stroke-width="1.2"/></svg>www.tallowbq.com.au</p>
</main>
</body>
</html>
```